BRAVEN POWERLINE SERVICES needs a vibrant design for electrical contracting work.

I require a card design for my own electrical contracting business. I will be doing a lot of domestic and commercial work, including things such as repairs, maintenance, lighting, installations and various others. LED lighting and energy efficiency will be a big part of my business. I wish not to have childish pictures such as light bulbs in the design, but rather a smart and modern looking card which incorporates my logo colours and perhaps the same lighting strike within the faded background of the card.

Target Market(s)

Residential and Commercial property owners.

Industry/Entity Type

Electrical

Contact Information for Business Card

Dalen Voskic
EC40923
Phone Number: 0417 358 942
Email: dalen@bravenpowerline.com

Font styles to use
Serif
Sans Serif

Requirements
Must have
• My Logo and associated colours.
Nice to have
• Some form of shapes splitting the card into different colours related to the colours of my logo. Electric Blue, Silver/Grey and White.
Should not have
• Childish pictures and symbols such as light bulbs.

```html
<!DOCTYPE html>
<html lang="en">
<head>
<meta charset="utf-8">
<title>Braven Powerline Services – Business Card</title>
<link rel="stylesheet" href="https://fonts.googleapis.com/css2?family=Roboto:wght@400;700&display=swap">
<style>
  :root {
    --backdrop: #b9babd;
    --electric-blue: #0a50a8;
    --silver-light: #f4f4f5;
    --silver-mid: #d9dadc;
    --white: #ffffff;
    --card-shadow: rgba(0, 0, 0, 0.28);
  }
  * { margin: 0; padding: 0; box-sizing: border-box; }
  html, body {
    width: 1200px;
    height: 1000px;
    overflow: hidden;
    background: var(--backdrop);
    font-family: "Roboto", Arial, sans-serif;
  }
  .stage {
    width: 1200px;
    height: 1000px;
    display: flex;
    align-items: center;
    justify-content: center;
  }
  .business-card {
    position: relative;
    width: 840px;
    height: 480px;
    border-radius: 6px;
    overflow: hidden;
    box-shadow: 0 18px 40px var(--card-shadow);
    background: radial-gradient(ellipse at 55% 35%, var(--silver-light) 0%, var(--silver-mid) 75%);
  }
  .card-shapes {
    position: absolute;
    inset: 0;
    width: 100%;
    height: 100%;
  }
  .brand {
    position: absolute;
    top: 96px;
    left: 0;
    right: 0;
    display: flex;
    align-items: center;
    justify-content: center;
    gap: 18px;
  }
  .brand-dot {
    width: 54px;
    height: 54px;
    border-radius: 50%;
    background: var(--electric-blue);
  }
  .brand-name {
    font-size: 40px;
    font-weight: 700;
    letter-spacing: 1px;
    color: var(--electric-blue);
  }
  .contact {
    position: absolute;
    left: 0;
    right: 0;
    top: 372px;
    color: var(--white);
    text-align: center;
  }
  .contact-name {
    font-size: 28px;
    font-weight: 700;
    margin-bottom: 14px;
  }
  .contact-lines {
    display: flex;
    justify-content: center;
    gap: 40px;
    font-size: 20px;
  }
  .contact-item {
    display: flex;
    align-items: center;
    gap: 8px;
  }
  .contact-item svg { width: 20px; height: 20px; fill: var(--white); }
</style>
</head>
<body>
<main class="stage">
  <section class="business-card" aria-label="Braven Powerline Services business card">
    <svg class="card-shapes" viewBox="0 0 840 480" preserveAspectRatio="none" aria-hidden="true">
      <polygon class="strike-white" fill="var(--white)"
        points="0,222 290,236 245,276 520,296 480,326 840,352 840,380 480,350 520,320 250,300 300,258 0,250"/>
      <polygon class="band-blue" fill="var(--electric-blue)"
        points="0,250 300,258 250,300 520,320 480,350 840,380 840,480 0,480"/>
    </svg>

    <div class="brand">
      <span class="brand-dot"></span>
      <span class="brand-name">BRAVEN POWERLINE SERVICES</span>
    </div>

    <div class="contact">
      <p class="contact-name">Dalen Voskic EC40923</p>
      <div class="contact-lines">
        <span class="contact-item">
          <svg viewBox="0 0 24 24"><path d="M6.6 10.8c1.4 2.8 3.8 5.1 6.6 6.6l2.2-2.2c.3-.3.7-.4 1-.2 1.1.4 2.3.6 3.6.6.6 0 1 .4 1 1V20c0 .6-.4 1-1 1C10.6 21 3 13.4 3 4c0-.6.4-1 1-1h3.5c.6 0 1 .4 1 1 0 1.3.2 2.5.6 3.6.1.3 0 .7-.2 1z"/></svg>
          0417 358 942
        </span>
        <span class="contact-item">
          <svg viewBox="0 0 24 24"><path d="M2 5h20v14H2zM4 7v.5l8 5 8-5V7l-8 5z"/></svg>
          dalen@bravenpowerline.com
        </span>
      </div>
    </div>
  </section>
</main>
</body>
</html>
```